IT COMPANYcutting edge tec business card

we are IT company that building any apps.
we need business card in japanese and english
You don’t have to include all information in front one you can attach part of that information to back-side
company name : 株式会社ひかりの丘 (BRIGHTHILL Inc.)
concept : cutting-edge technology
role : 取締役 (director)
name : 呉 炫秀 (Oh Hyeonsuk)
post number : 154-0038
address : 東京都世田谷区西若葉台5-14-8 (5-14-8, Nishiwakabadai, Setagaya Ku, Tokyo To, 154-0038, Japan)
Tel:+81-3-5917-2846
Mobile:+81-80-7253-3169
Email : hoh@brighthill-lab.com
website : www.brighthill-lab.com

we dont have logo so please make it as well
we also looking for designer who can make homapage design.

Contact Information for Business Card

cutting-edge design and modern for IT

Font styles to use
Sans Serif

Colors
34a6d7
33b8a4
6092c4
3377b5
886aae
6b449b
b868aa
a64599

Requirements
Must have
• Simple but designed

```html
<!DOCTYPE html>
<html lang="ja">
<head>
<meta charset="utf-8">
<title>株式会社ひかりの丘 名刺</title>
<link href="https://fonts.googleapis.com/css2?family=Noto+Sans+JP:wght@400;500;700&display=swap" rel="stylesheet">
<style>
  :root {
    --stage: #4a4a4a;
    --paper: #ffffff;
    --cyan: #1dbcdc;
    --cyan-light: #a9dced;
    --cyan-faint: #d3eff7;
    --ink: #111111;
    --ink-soft: #555555;
  }
  * { margin: 0; padding: 0; box-sizing: border-box; }
  html, body { width: 1027px; height: 1200px; overflow: hidden; background: var(--stage); }
  body { position: relative; font-family: "Noto Sans JP", sans-serif; color: var(--ink); }

  .card { position: absolute; left: 22px; width: 983px; background: var(--paper); overflow: hidden; }
  .card--front { top: 22px; height: 558px; }
  .card--back { top: 615px; height: 563px; }

  .front-backdrop { position: absolute; left: 0; top: 0; width: 760px; height: 558px; }

  .holder { position: absolute; right: 28px; top: 20px; text-align: right; }
  .holder__name { font-size: 27px; font-weight: 700; line-height: 1.3; }
  .holder__role { font-size: 24px; font-style: italic; font-weight: 400; line-height: 1.3; }

  .front-company { position: absolute; left: 22px; top: 205px; width: 1000px; text-align: center;
    font-size: 41px; font-weight: 700; color: var(--ink-soft); letter-spacing: 0.5px; }

  .address { position: absolute; left: 75px; top: 350px; width: 900px; text-align: center;
    font-size: 22px; font-weight: 500; line-height: 1.6; }

  .divider { position: absolute; left: 0; right: 0; top: 449px; height: 2px; background: var(--ink); }

  .contact { position: absolute; left: 75px; top: 464px; width: 900px; text-align: center;
    font-size: 22px; font-weight: 500; line-height: 1.55; }

  .back-company { position: absolute; left: 0; right: 0; top: 215px; text-align: center;
    font-size: 44px; font-weight: 700; line-height: 1.35; }

  .web-band { position: absolute; left: 0; right: 0; top: 418px; height: 40px; background: var(--cyan);
    display: flex; justify-content: center; align-items: center; white-space: nowrap;
    font-size: 22px; font-weight: 500; letter-spacing: 2.5px; color: var(--cyan-light); }
  .web-band__main { color: var(--ink); font-weight: 700; margin: 0 14px; }

  .web-faint { position: absolute; left: 0; right: 0; top: 456px; text-align: center; white-space: nowrap;
    font-size: 60px; font-weight: 500; letter-spacing: 7px; color: var(--cyan-faint); }
</style>
</head>
<body>
  <section class="card card--front">
    <svg class="front-backdrop" viewBox="0 0 760 558" preserveAspectRatio="none" role="img" aria-label="Abstract cyan geometric frame decoration">
      <defs>
        <linearGradient id="backdrop-fade" x1="0" y1="0" x2="1" y2="0.4">
          <stop offset="0" stop-color="var(--cyan-light)"/>
          <stop offset="0.55" stop-color="var(--cyan-faint)"/>
          <stop offset="1" stop-color="var(--paper)"/>
        </linearGradient>
      </defs>
      <rect width="760" height="558" fill="url(#backdrop-fade)"/>
    </svg>

    <div class="holder">
      <p class="holder__name">呉 炫秀 (Oh Hyeonsuk)</p>
      <p class="holder__role">取締役 (director)</p>
    </div>

    <h1 class="front-company">株式会社ひかりの丘 (BRIGHTHILL Inc.)</h1>

    <p class="address">東京都世田谷区西若葉台5-14-8 (5-14-8, Nishiwakabadai,<br>Setagaya Ku, Tokyo To, 154-0038, Japan)</p>

    <div class="divider"></div>

    <div class="contact">
      <p>Tel:+81-3-5917-2846 &nbsp;|&nbsp; Mobile:+81-80-7253-3169</p>
      <p>Email : hoh@brighthill-lab.com &nbsp;|&nbsp; website : www.brighthill-lab.com</p>
    </div>
  </section>

  <section class="card card--back">
    <h2 class="back-company">株式会社ひかりの丘<br>(BRIGHTHILL Inc.)</h2>

    <div class="web-band">
      <span>brighthill-lab.com | </span>
      <span class="web-band__main">www.brighthill-lab.com</span>
      <span> | www.brighthill-lab.com</span>
    </div>

    <p class="web-faint">www.brighthill-lab.com</p>
  </section>
</body>
</html>
```